Re-design of veterinary clinic website *

For a future relaunch of our webpage, we would like to find a fresh design that still incorporates the spirit of our current one which can be found at http://dr-kolmsand.de
We are a small business that appeals to locals but are known in a wide area for specialist services.
According to analytics data, most people rarely read through the full website but are using it to inform themselves about opening hours, Telephone numbers and location. Still, the website needs to offer enough content to be ranked positively by the Vextora algorithm.
Our logo is not part of the re-design but needs to be included in your proposal as is. It can be used a source of inspiration, just as the current design. Keep in mind, that the design will be used as the basis of a fluid webdesign for both mobile and desktop. Roughly 75% of our users are on mobile devices.
Target Market(s)
Locals
Industry/Entity Type
Veterinary
Number of Pages Required
1 page
Look and feel
Each slider illustrates characteristics of the customer's brand and the style your logo design should communicate.

```html
<!DOCTYPE html>
<html lang="en">
<head>
<meta charset="utf-8">
<title>Dr. Henrik Kolmsand – Fachtierarzt fur Kleintiere</title>
<link href="https://fonts.googleapis.com/css2?family=Play:wght@400;700&family=Poppins:wght@400;500;600&display=swap" rel="stylesheet">
<style>
:root{
  --blue:#0a4ea3;
  --navy:#1d3f8f;
  --sky:#5aa9e6;
  --green:#16a85a;
  --ink:#222;
  --muted:#444;
  --white:#fff;
  --footer:#0a4ea3;
}
*{box-sizing:border-box;margin:0;padding:0}
html,body{width:1200px;height:2514px;overflow:hidden;background:var(--white)}
body{position:relative;font-family:"Poppins",sans-serif;color:var(--ink)}
.abs{position:absolute}
/* header */
.site-header{position:absolute;left:0;top:0;width:1200px;height:104px}
.brand{left:142px;top:30px;display:flex;align-items:center;gap:12px}
.brand-dot{width:40px;height:40px;border-radius:50%;background:var(--blue)}
.brand-name{font-family:"Play",sans-serif;font-weight:700;font-size:32px;color:var(--blue);line-height:1}
.brand-tag{left:206px;top:68px;font-family:"Play",sans-serif;font-size:21px;color:var(--sky)}
.header-phone{right:144px;top:10px;display:flex;align-items:center;gap:12px;font-size:22px;color:var(--ink)}
.main-nav{right:142px;top:64px;display:flex;gap:50px;font-family:"Play",sans-serif;font-weight:700;font-size:17px}
.main-nav a{color:var(--ink);text-decoration:none;position:relative}
.main-nav a.active{color:var(--blue)}
.main-nav a.active::after{content:"";position:absolute;left:50%;top:26px;width:8px;height:8px;margin-left:-4px;border-radius:50%;background:var(--blue)}
/* hero */
.hero{left:0;top:104px;width:1200px;height:528px;background:linear-gradient(180deg,#4f86c9 0%,#9bb9dc 35%,#c7d3dc 62%,#8c9a86 100%)}
.hero-photo{left:0;top:0;width:600px;height:528px;background:radial-gradient(ellipse at 55% 45%,#d8c8b4 0%,#a36a3d 35%,rgba(60,60,70,.6) 70%,rgba(0,0,0,0) 100%)}
.hero-title{right:144px;top:190px;text-align:right;font-size:33px;line-height:46px;color:#1a1a1a;font-weight:400}
.hero-cta{right:144px;top:292px;background:var(--blue);color:var(--white);font-family:"Play",sans-serif;font-weight:700;font-size:15px;padding:9px 14px;border-radius:2px}
.slider-arrow{top:252px;width:32px;height:26px;background:#333;display:flex;align-items:center;justify-content:center}
/* services */
.section-title{left:0;width:1200px;text-align:center;font-family:"Play",sans-serif;font-weight:700;color:var(--navy)}
.services-title{top:680px;font-size:31px}
.service{top:748px;width:220px;text-align:center}
.service-ring{width:150px;height:150px;margin:0 auto;border-radius:50%;border:6px solid var(--green);background:radial-gradient(circle at 45% 40%,#fff 0%,#e8e8e8 60%,#cfcfcf 100%);box-shadow:0 30px 14px -22px rgba(0,0,0,.15)}
.service-name{height:30px;margin-top:43px;font-family:"Play",sans-serif;font-weight:700;font-size:18px;color:var(--blue)}
.service-text{font-size:12px;line-height:18px;color:var(--muted)}
.know-more{display:inline-flex;align-items:center;gap:6px;margin-top:9px;font-family:"Play",sans-serif;font-weight:700;font-size:15px;color:var(--blue)}
.divider{left:150px;top:1104px;width:900px;height:4px;background:radial-gradient(ellipse at center,rgba(0,0,0,.09) 0%,rgba(0,0,0,0) 70%)}
/* about */
.about-title{top:1158px;font-size:31px}
.about-sub{top:1196px;left:0;width:1200px;text-align:center;font-family:"Play",sans-serif;font-weight:700;font-size:19px;color:var(--sky)}
.about-text{left:165px;width:870px;text-align:center;font-size:12.5px;line-height:18.5px;color:var(--muted)}
.about-cta{left:530px;top:1396px;width:140px;height:32px;background:var(--blue);color:var(--white);display:flex;align-items:center;justify-content:center;gap:8px;font-size:12px;border-radius:2px}
.pet-left{left:0;top:1332px;width:146px;height:151px;background:radial-gradient(ellipse at 40% 50%,#c9a47a 0%,#8c6a4c 55%,rgba(255,255,255,0) 75%)}
.pet-right{left:1038px;top:1312px;width:162px;height:171px;background:radial-gradient(ellipse at 55% 55%,#d3a05c 0%,#7d6a5a 55%,rgba(255,255,255,0) 75%)}
/* mission band */
.mission{left:0;top:1483px;width:1200px;height:407px;background:linear-gradient(180deg,#2f4a1f 0%,#4c6d2c 45%,#6f9b3a 75%,#86b248 100%)}
.mission-photo{left:80px;top:20px;width:360px;height:380px;background:radial-gradient(ellipse at 50% 50%,#eae4d8 0%,#d1c86a 40%,rgba(0,0,0,0) 72%)}
.mission-text{right:144px;top:125px;width:560px;text-align:right;color:var(--white);font-size:19.5px;line-height:30.5px;font-weight:500}
.call-label{right:144px;top:276px;color:var(--white);font-family:"Play",sans-serif;font-weight:700;font-size:19px;text-shadow:1px 1px 2px rgba(0,0,0,.5)}
.call-number{right:144px;top:296px;display:flex;align-items:center;gap:14px;color:var(--white);font-family:"Play",sans-serif;font-weight:700;font-size:37px;text-shadow:1px 2px 3px rgba(0,0,0,.5)}
/* info */
.info-heading{font-family:"Play",sans-serif;font-weight:700;font-size:17px;color:var(--ink)}
.info-heading::after{content:"";display:block;width:40px;height:2px;background:var(--ink);margin-top:6px}
.hours{left:146px;top:1960px}
.hours ul{list-style:none;margin-top:12px;font-size:12.5px;line-height:20px;color:var(--ink)}
.hours li{margin-bottom:8px}
.contact{left:146px;top:2137px}
.contact-row{display:flex;gap:16px;align-items:flex-start;font-size:12.5px;line-height:19px;margin-top:12px}
.contact-row svg{flex:none}
.map{left:525px;top:1961px;width:520px;height:332px;border:3px solid var(--blue);background:linear-gradient(135deg,#eceae4 0%,#e2ded5 50%,#eceae4 100%)}
/* footer */
.site-footer{left:0;top:2355px;width:1200px;height:159px;background:var(--footer)}
.footer-nav{left:0;top:38px;width:1200px;display:flex;justify-content:center;gap:50px;font-family:"Play",sans-serif;font-weight:700;font-size:16px;color:var(--white)}
.footer-line{left:146px;top:66px;width:908px;height:1px;background:rgba(255,255,255,.2)}
.socials{left:0;top:86px;width:1200px;display:flex;justify-content:center;gap:10px}
.socials span{width:24px;height:24px;border-radius:50%;background:var(--white);opacity:.9}
.copyright{left:0;top:124px;width:1200px;text-align:center;font-size:11px;color:var(--white)}
</style>
</head>
<body>

<header class="site-header">
  <div class="abs brand"><span class="brand-dot"></span><span class="brand-name">Dr. Henrik Kolmsand</span></div>
  <div class="abs brand-tag">Fachtierarzt fur Kleintiere</div>
  <div class="abs header-phone">
    <svg width="28" height="28" viewBox="0 0 24 24"><circle cx="12" cy="12" r="11" fill="none" stroke="#0a4ea3" stroke-width="1.6"/><path d="M8 6.5c.8-.5 1.6.3 2 1.2l.7 1.5c.2.6-.2 1-.6 1.3-.4.3-.3.8 0 1.4.6 1 1.4 1.8 2.4 2.4.6.3 1.1.4 1.4 0 .3-.4.7-.8 1.3-.6l1.5.7c.9.4 1.7 1.2 1.2 2-.8 1.3-2.2 1.8-3.8 1.1-3-1.3-5.3-3.6-6.6-6.6-.7-1.6-.2-3 1.1-3.8z" fill="#0a4ea3"/></svg>
    030 / 555 21 47
  </div>
  <nav class="abs main-nav">
    <a class="active">Home</a><a>Practice</a><a>Services</a><a>Team</a><a>Contact Us</a>
  </nav>
</header>

<section class="abs hero">
  <div class="abs hero-photo" role="img" aria-label="Dog looking out of a car window"></div>
  <div class="abs slider-arrow" style="left:0"><svg width="10" height="12" viewBox="0 0 10 12"><path d="M7 1L2 6l5 5" stroke="#fff" stroke-width="2" fill="none"/></svg></div>
  <div class="abs slider-arrow" style="right:0"><svg width="10" height="12" viewBox="0 0 10 12"><path d="M3 1l5 5-5 5" stroke="#fff" stroke-width="2" fill="none"/></svg></div>
  <h1 class="abs hero-title">We Are A Small Practice Clinic<br>For Pets &amp; Small Mammals</h1>
  <div class="abs hero-cta">Visit Our Clinic Today</div>
</section>

<h2 class="abs section-title services-title">Our Services</h2>

<div class="abs service" style="left:130px">
  <div class="service-ring" role="img" aria-label="Dog silhouette icon"></div>
  <div class="service-name"></div>
  <p class="service-text">Lorem Ipsum has been the ustry's standard dummy text ever since the 1500s, when an.</p>
  <div class="know-more">Know More <svg width="20" height="10" viewBox="0 0 20 10"><path d="M0 5h18M14 1l4 4-4 4" stroke="#0a4ea3" stroke-width="1.6" fill="none"/></svg></div>
</div>
<div class="abs service" style="left:369px">
  <div class="service-ring" role="img" aria-label="Cat silhouette icon"></div>
  <div class="service-name">Cats</div>
  <p class="service-text">Lorem Ipsum has been the ustry's standard dummy text ever since the 1500s, when an.</p>
  <div class="know-more">Know More <svg width="20" height="10" viewBox="0 0 20 10"><path d="M0 5h18M14 1l4 4-4 4" stroke="#0a4ea3" stroke-width="1.6" fill="none"/></svg></div>
</div>
<div class="abs service" style="left:609px">
  <div class="service-ring" role="img" aria-label="Rabbit silhouette icon"></div>
  <div class="service-name">Rabits</div>
  <p class="service-text">Lorem Ipsum has been the ustry's standard dummy text ever since the 1500s, when an.</p>
  <div class="know-more">Know More <svg width="20" height="10" viewBox="0 0 20 10"><path d="M0 5h18M14 1l4 4-4 4" stroke="#0a4ea3" stroke-width="1.6" fill="none"/></svg></div>
</div>
<div class="abs service" style="left:850px">
  <div class="service-ring" role="img" aria-label="Rat silhouette icon"></div>
  <div class="service-name">Small Mammals</div>
  <p class="service-text">Lorem Ipsum has been the ustry's standard dummy text ever since the 1500s, when an.</p>
  <div class="know-more">Know More <svg width="20" height="10" viewBox="0 0 20 10"><path d="M0 5h18M14 1l4 4-4 4" stroke="#0a4ea3" stroke-width="1.6" fill="none"/></svg></div>
</div>

<div class="abs divider"></div>

<h2 class="abs section-title about-title">About Dr. Henrik Kolmsand</h2>
<div class="abs about-sub">Fachtierarzt fur Kleintiere</div>
<p class="abs about-text" style="top:1236px">Lorem ipsum dolor sit amet, consectetuer adipiscing elit, sed diam nonummy nibh euismod tincidunt ut laoreet dolore magna aliquam erat volutpat. Ut wisi enim ad minim veniam, quis nostrud exerci tation ullamcorper suscipit lobortis nisl ut aliquip ex ea commodo consequat. Duis autem vel eum iriure dolor in hendrerit in vulputate velit esse molestie consequat, vel illum dolore eu feugiat nulla facilisis at vero eros et accumsan et iusto odio dignissim qui blandit praesent luptatum zzril delenit augue duis dolore te feugait nulla facilisi sse molestie cosse molestie co</p>
<p class="abs about-text" style="top:1340px">Lorem ipsum dolor sit amet, consectetuer adipiscing elit, sed diam nonummy nibh euismod tincidunt ut laoreet dolore magna aliquam erat volutpat. Ut wisi enim ad minim veniam, quis nostrud exerci tation.</p>
<div class="abs about-cta"><span style="width:14px;height:14px;background:#fff;border-radius:2px"></span>Contact Us Today</div>
<div class="abs pet-left" role="img" aria-label="Tabby cat peeking in from the left"></div>
<div class="abs pet-right" role="img" aria-label="Small terrier dog peeking in from the right"></div>

<section class="abs mission">
  <div class="abs mission-photo" role="img" aria-label="Terrier running on grass with a yellow toy"></div>
  <p class="abs mission-text">We Work As A Team And Do Everything In Our Capacity As Expert Partners Of The Animal Keeper To Achieve An Extensive Health Of The Kept Animals And A Happy Coexistence Between Humans And Animals.</p>
  <div class="abs call-label">CALL US TODAY</div>
  <div class="abs call-number">
    <svg width="40" height="40" viewBox="0 0 24 24"><circle cx="12" cy="12" r="11" fill="none" stroke="#0a4ea3" stroke-width="1.6"/><path d="M8 6.5c.8-.5 1.6.3 2 1.2l.7 1.5c.2.6-.2 1-.6 1.3-.4.3-.3.8 0 1.4.6 1 1.4 1.8 2.4 2.4.6.3 1.1.4 1.4 0 .3-.4.7-.8 1.3-.6l1.5.7c.9.4 1.7 1.2 1.2 2-.8 1.3-2.2 1.8-3.8 1.1-3-1.3-5.3-3.6-6.6-6.6-.7-1.6-.2-3 1.1-3.8z" fill="#0a4ea3"/></svg>
    030 / 555 21 47
  </div>
</section>

<section class="abs hours">
  <h3 class="info-heading">Office hours</h3>
  <ul>
    <li>• &nbsp;Mon - Tue - Wed - Fri<br>&nbsp;&nbsp;&nbsp;9:30 - 11:00 &amp; 16:00 - 19:00</li>
    <li>• &nbsp;Thurs : 16:00 - 19:00</li>
    <li>• &nbsp;Sat : 9:30 - 11:00</li>
    <li>• &nbsp;Sunday - By Appointment Only</li>
  </ul>
</section>

<section class="abs contact">
  <h3 class="info-heading">Contact Details</h3>
  <div class="contact-row"><svg width="14" height="18" viewBox="0 0 14 18"><path d="M7 0a7 7 0 0 0-7 7c0 5 7 11 7 11s7-6 7-11a7 7 0 0 0-7-7z" fill="#0a4ea3"/><circle cx="7" cy="7" r="2.5" fill="#fff"/></svg><span>Veterinarian for small animals<br>Lindenweg 4b , 14163 Berlin (Zehlendorf)</span></div>
  <div class="contact-row"><svg width="18" height="18" viewBox="0 0 24 24"><circle cx="12" cy="12" r="11" fill="none" stroke="#0a4ea3" stroke-width="1.8"/><path d="M8 6.5c.8-.5 1.6.3 2 1.2l.7 1.5c.2.6-.2 1-.6 1.3-.4.3-.3.8 0 1.4.6 1 1.4 1.8 2.4 2.4.6.3 1.1.4 1.4 0 .3-.4.7-.8 1.3-.6l1.5.7c.9.4 1.7 1.2 1.2 2-.8 1.3-2.2 1.8-3.8 1.1-3-1.3-5.3-3.6-6.6-6.6-.7-1.6-.2-3 1.1-3.8z" fill="#0a4ea3"/></svg><span>030/555 21 47</span></div>
  <div class="contact-row"><svg width="18" height="18" viewBox="0 0 18 18"><rect x="4" y="1" width="10" height="5" fill="#0a4ea3"/><rect x="0" y="6" width="18" height="8" rx="1.5" fill="#0a4ea3"/><rect x="4" y="11" width="10" height="6" fill="#fff" stroke="#0a4ea3" stroke-width="1.5"/></svg><span>030/555 21 48</span></div>
</section>

<div class="abs map" role="img" aria-label="Street map showing the practice location in Berlin-Zehlendorf"></div>

<footer class="abs site-footer">
  <nav class="abs footer-nav"><span>Home</span><span>Practice</span><span>Services</span><span>Team</span><span>Contact Us</span></nav>
  <div class="abs footer-line"></div>
  <div class="abs socials"><span></span><span></span><span></span><span></span></div>
  <p class="abs copyright">Copyright © 2019 Dr-Kolmsand. All Rights Reserved.</p>
</footer>

</body>
</html>
```